Best website on the WWW

I am looking to create a multi tab wesbite to revamp our outdated website.

Here is an example of a companies website I really like
https://ridgelinehaulers.example/

Target Market(s)

New customers, government agency's

Industry/Entity Type

Auto repair, towing and recovery, hazmat clean up

Coding

Coded - Design and coding required

Number of Pages Required

5+ page

Font styles to use
Sans Serif

Requirements
Nice to have
• I would like to see an interactive website, that includes details and photos from our companies

```html
<!DOCTYPE html>
<html lang="en">
<head>
<meta charset="utf-8">
<title>Ridgeline Repair &amp; Towing</title>
<link href="https://fonts.googleapis.com/css2?family=Rajdhani:wght@500;600;700&family=Montserrat:wght@400;500;600&display=swap" rel="stylesheet">
<style>
:root{
  --accent:#e5173f;
  --red:#e41b23;
  --navy:#0f2a56;
  --blue:#2d74d2;
  --deep-blue:#17549f;
  --dark:#1c2434;
  --darker:#161d2a;
  --ink:#1d1d1d;
  --muted:#6c6f76;
  --light:#eef0f4;
  --white:#fff;
  --head:'Rajdhani',sans-serif;
  --body:'Montserrat',sans-serif;
}
*{box-sizing:border-box;margin:0;padding:0}
html,body{width:1200px;height:3807px;overflow:hidden}
body{font-family:var(--body);color:var(--ink);background:var(--white);position:relative}
section,header,footer,nav{position:absolute;left:0;width:1200px}
.abs{position:absolute}
.hl{display:inline-block;background:var(--accent);color:#fff;font-style:italic;font-weight:500;padding:0 14px;transform:skewX(-20deg);margin-left:6px}
.hl span{display:inline-block;transform:skewX(20deg)}
.sec-title{font-family:var(--head);font-weight:700;text-align:center;width:100%;font-size:29px;letter-spacing:.5px;text-transform:uppercase}
.sec-title .hl{text-transform:none;font-size:30px}
.btn{position:absolute;display:flex;align-items:center;justify-content:center;font-size:10px;font-weight:600;letter-spacing:.5px;color:#fff;background:var(--red);text-transform:uppercase}

/* header */
.topbar{top:0;height:66px;background:#fff}
.brand{left:130px;top:14px;font-family:var(--head);font-weight:700;font-size:20px;color:var(--navy);line-height:1.05;display:flex;align-items:center;gap:8px}
.brand i{display:block;width:14px;height:14px;border-radius:50%;background:var(--accent)}
.contact-item{top:16px;display:flex;gap:10px;align-items:center}
.contact-item small{display:block;font-size:9px;color:var(--ink)}
.contact-item b{font-weight:400;font-size:13px}
.btn-schedule{left:927px;top:15px;width:144px;height:35px;background:var(--blue);font-weight:500;letter-spacing:0;text-transform:none;font-size:10px}
.mainnav{top:66px;height:36px;background:var(--navy)}
.mainnav a{position:absolute;top:11px;font-size:11px;color:#fff;text-decoration:none;letter-spacing:.3px;text-transform:uppercase}
.mainnav a.active{color:var(--accent)}
.mainnav .sep{position:absolute;top:10px;width:1px;height:16px;background:rgba(255,255,255,.2)}
.more{left:1011px;top:12px;font-size:9px;color:#fff;letter-spacing:1px}
.burger{left:1046px;top:12px;width:24px}
.burger i{display:block;height:2px;background:#fff;margin-bottom:3px}

/* hero */
.hero{top:102px;height:464px;background:linear-gradient(110deg,#3d4047,#5a5e66 45%,#6a6e75 70%,#444850)}
.hero .shade{position:absolute;inset:0;background:rgba(10,14,24,.35)}
.hero-tag{top:116px;width:100%;text-align:center;font-family:var(--head);font-weight:700;font-size:26px;color:var(--accent)}
.hero-tag .hl{font-size:19px;padding:2px 12px}
.hero h1{top:165px;width:100%;text-align:center;font-family:var(--head);font-weight:700;font-size:60px;color:#fff;letter-spacing:1px}
.hero p{top:246px;left:220px;width:760px;text-align:center;font-size:12px;line-height:19px;color:#fff;font-weight:500}
.dot-arrow{top:419px;width:26px;height:26px;border-radius:50%;background:rgba(255,255,255,.35);color:#fff;display:flex;align-items:center;justify-content:center;font-size:12px}

/* welcome */
.welcome{top:566px;height:392px;background:linear-gradient(160deg,#242b39,#1b2130 60%,#262d3c)}
.welcome .eyebrow{top:66px;width:100%;text-align:center;font-size:11px;color:#fff}
.welcome .sec-title{top:94px;color:#fff}
.welcome p{top:157px;left:255px;width:690px;text-align:center;color:#fff;font-size:12px;line-height:19.5px}
.btn-outline{background:transparent;border:2px solid var(--red)}

/* customer services */
.customer{top:958px;height:536px}
.customer .eyebrow{top:60px;width:100%;text-align:center;font-size:11px;color:var(--ink)}
.customer .sec-title{top:84px}
.svc-card{top:150px;width:300px;text-align:center}
.svc-photo{width:230px;height:230px;border-radius:50%;margin:0 auto;background:linear-gradient(150deg,#8b8f96,#4f545b)}
.svc-card h3{margin-top:14px;font-family:var(--head);font-style:italic;font-weight:600;font-size:18px}
.svc-card p{margin-top:12px;font-size:11.5px;line-height:17.5px;color:var(--muted)}

/* our services */
.our{top:1494px;height:504px;background:linear-gradient(120deg,#1f2839,#1a2232)}
.our .sec-title{top:58px;color:#fff}
.svc-list{left:130px;width:250px}
.svc-list h4{font-family:var(--head);font-style:italic;font-weight:600;font-size:12px;color:#fff;text-transform:uppercase}
.svc-list h4::before{content:"\2022 ";color:var(--accent)}
.svc-list h4 em{color:var(--accent)}
.svc-list p{margin:6px 0 0 8px;font-size:11px;line-height:15px;color:#fff}
.feature-photo{left:389px;top:130px;width:479px;height:312px;background:linear-gradient(150deg,#d3d6db,#8d9197 55%,#54585f)}
.tab{top:130px;height:312px;width:63px;display:flex;align-items:center;justify-content:center}
.tab span{transform:rotate(-90deg);white-space:nowrap;font-family:var(--head);font-style:italic;font-weight:700;font-size:19px;color:#fff;text-transform:uppercase}

/* blog */
.blog{top:1998px;height:515px}
.blog .sec-title{top:56px}
.blog .tagline{top:101px;width:100%;text-align:center;font-size:9px;letter-spacing:4px;color:var(--muted)}
.post{top:136px;width:301px}
.post-photo{height:186px;background:linear-gradient(150deg,#b9bcc2,#55595f)}
.post-rule{height:5px;background:repeating-linear-gradient(45deg,var(--accent) 0 3px,#f47a95 3px 5px)}
.post h3{margin-top:17px;font-family:var(--head);font-weight:600;font-size:14.5px;text-transform:uppercase}
.post p{margin-top:10px;font-size:11px;line-height:15.5px;color:var(--muted)}
.post .btn{position:relative;width:98px;height:34px;margin-top:18px}

/* join / quote */
.split{top:2513px;height:402px}
.join{left:0;top:0;width:600px;height:402px;background:linear-gradient(140deg,#1b5daa,#154c92)}
.quote{left:600px;top:0;width:600px;height:402px;background:linear-gradient(140deg,#222a3a,#181f2d)}
.split h2{position:absolute;top:60px;width:100%;text-align:center;font-family:var(--head);font-weight:700;font-size:27px;color:#fff}
.split h2 .hl{font-size:28px}
.split .sub{position:absolute;top:100px;width:100%;text-align:center;font-size:10px;color:rgba(255,255,255,.75)}
.join p{position:absolute;left:130px;top:160px;width:400px;text-align:center;font-size:11.5px;line-height:18px;color:#fff}
.field{position:absolute;border:1px solid rgba(255,255,255,.35);font-size:9.5px;color:#fff;padding:10px 10px}
.hook{left:576px;top:0;width:48px;height:90px;background:linear-gradient(180deg,#e9b320,#3b3f46);border-radius:0 0 24px 24px}

/* testimonial */
.testimonial{top:2915px;height:473px;background:linear-gradient(90deg,#dfe2e8,#f1f2f5 50%,#e2e5ea)}
.avatar{left:550px;top:99px;width:100px;height:100px;border-radius:50%;background:linear-gradient(160deg,#cfd3d9,#6b7078);border:3px solid #fff}
.testimonial blockquote{position:absolute;left:230px;top:238px;width:740px;text-align:center;font-size:12px;line-height:20px;color:#333}
.testimonial h5{position:absolute;top:346px;width:100%;text-align:center;font-family:var(--head);font-weight:600;font-size:16px;color:var(--accent)}
.testimonial .role{top:370px;width:100%;text-align:center;font-size:11.5px}

/* footer */
.site-footer{top:3388px;height:419px;background:var(--dark)}
.footer-brand{left:130px;top:80px;font-family:var(--head);font-weight:700;font-size:28px;color:#fff;display:flex;align-items:center;gap:10px}
.footer-brand i{width:18px;height:18px;border-radius:50%;background:var(--accent);display:block}
.footer-about{left:130px;top:195px;width:360px;font-size:10.5px;line-height:18px;color:#fff}
.social{top:263px;width:32px;height:32px;border-radius:50%;border:1px solid rgba(255,255,255,.5)}
.fcol{top:60px}
.fcol h6{font-family:var(--head);font-weight:600;font-size:14px;color:#fff;text-transform:uppercase;letter-spacing:.3px}
.fcol h6 em{font-style:normal;color:var(--accent)}
.fcol ul{list-style:none;margin-top:12px}
.fcol li{font-size:10.5px;color:#fff;height:24px}
.citem{display:flex;gap:8px;font-size:10.5px;line-height:14px;color:#fff;margin-top:14px;align-items:center}
.citem i{flex:none;width:26px;height:26px;border-radius:50%;background:var(--accent);display:flex;align-items:center;justify-content:center}
.newsletter{left:850px;top:179px;width:219px;height:31px;background:#2a3447;font-size:9.5px;color:#fff;padding:10px}
.newsletter i{position:absolute;right:6px;top:5px;width:21px;height:21px;background:var(--accent);display:flex;align-items:center;justify-content:center}
.footer-rule{top:329px;left:0;width:1200px;height:1px;background:rgba(255,255,255,.1)}
.copy{top:352px;width:100%;text-align:center;font-size:9px;color:#fff}
.copy em{font-style:normal;color:var(--accent)}
</style>
</head>
<body>

<header class="topbar">
  <div class="brand abs"><i></i>RIDGELINE<br>REPAIR &amp; TOWING</div>
  <div class="contact-item abs" style="left:538px">
    <svg width="22" height="20" viewBox="0 0 22 20"><rect x="1" y="5" width="20" height="14" fill="none" stroke="#e5173f" stroke-width="1.5"/><path d="M1 5l10 8 10-8M5 5V1h12v4" fill="none" stroke="#e5173f" stroke-width="1.5"/></svg>
    <div><small>Mail Us</small><b>info@ridgelinerepair.example</b></div>
  </div>
  <div class="contact-item abs" style="left:776px">
    <svg width="20" height="20" viewBox="0 0 20 20"><path d="M4 1l4 4-2 3c1 3 3 5 6 6l3-2 4 4-3 3C8 18 2 12 1 4z" fill="none" stroke="#e5173f" stroke-width="1.5"/></svg>
    <div><small>Call Us</small><b>555-018-2740</b></div>
  </div>
  <div class="btn btn-schedule">Schedule A Maintenence</div>
</header>

<nav class="mainnav">
  <a class="active" style="left:130px">Home</a><span class="sep" style="left:183px"></span>
  <a style="left:207px">About Us</a><span class="sep" style="left:282px"></span>
  <a style="left:306px">Monthly Coupons</a><span class="sep" style="left:430px"></span>
  <a style="left:454px">Services</a><span class="sep" style="left:527px"></span>
  <a style="left:551px">Contacts</a>
  <span class="more abs">MORE</span>
  <div class="burger abs"><i></i><i></i><i></i></div>
</nav>

<section class="hero">
  <div class="abs" style="inset:0" role="img" aria-label="Tow truck and heavy wrecker parked in the shop yard"></div>
  <div class="shade"></div>
  <div class="hero-tag abs">TOWING <span class="hl"><span>FAMILY OWNED</span></span></div>
  <h1 class="abs">AUTO &amp; TRUCK REPAIR</h1>
  <p class="abs">We specialize in Towing, Auto Repair and most Truck Repairs of any size. From driving your daily pickup to your fleet of vehicles auto and truck repair towing service...</p>
  <div class="dot-arrow abs" style="left:1008px">&#8249;</div>
  <div class="dot-arrow abs" style="left:1042px">&#8250;</div>
</section>

<section class="welcome" role="img" aria-label="Dark background with close-up of an off-road wheel and tire">
  <div class="eyebrow abs">WELCOME</div>
  <h2 class="sec-title abs">Ridgeline <span class="hl"><span>Repair</span></span> and Towing</h2>
  <p class="abs">We now provide our customers with the ability to check their vehicle history on line! We will also send you email reminders when it is time to have your vehicle serviced according to your specific vehicle manufacture. Ask us how to get you registered today!</p>
  <div class="btn" style="left:500px;top:238px;width:96px;height:33px">Read More</div>
  <div class="btn btn-outline" style="left:606px;top:238px;width:96px;height:33px">Get Started</div>
</section>

<section class="customer">
  <div class="eyebrow abs">FAST AND FRIENDLY</div>
  <h2 class="sec-title abs">Customer <span class="hl"><span>Services</span></span></h2>
  <svg class="abs" style="left:380px;top:140px" width="130" height="60" viewBox="0 0 130 60"><path d="M8 52C20 10 70 0 115 26" fill="none" stroke="#222" stroke-width="5" stroke-linecap="round"/><path d="M96 16l24 12-24 8" fill="none" stroke="#222" stroke-width="5" stroke-linecap="round" stroke-linejoin="round"/></svg>
  <svg class="abs" style="left:700px;top:330px" width="130" height="60" viewBox="0 0 130 60"><path d="M6 6c10 44 60 52 108 24" fill="none" stroke="#222" stroke-width="5" stroke-linecap="round"/><path d="M94 22l24 6-14 20" fill="none" stroke="#222" stroke-width="5" stroke-linecap="round" stroke-linejoin="round"/></svg>
  <div class="svc-card abs" style="left:129px"><div class="svc-photo" role="img" aria-label="Technician working on chrome wheels and tires"></div><h3>Experienced Technicians</h3><p>The mechanics at our shop have over 60 years of experience between them. They are dedicated to providing high-quality repairs...</p></div>
  <div class="svc-card abs" style="left:450px"><div class="svc-photo" role="img" aria-label="Red and white tow truck in the snow" style="background:linear-gradient(160deg,#c9d3df,#8d9199)"></div><h3>Competitive Pricing</h3><p>Whether you're coming in for a routine inspection or a repair service, we promise that you will be completely satisfied...</p></div>
  <div class="svc-card abs" style="left:769px"><div class="svc-photo" role="img" aria-label="Off-road tire on a black custom rim" style="background:linear-gradient(150deg,#6d6f74,#2a2c30)"></div><h3>Our Quality Promise</h3><p>We're committed to providing a stress free experience to both new and returning customers.</p></div>
</section>

<section class="our">
  <h2 class="sec-title abs"><span style="color:#fff">Our</span> <span class="hl"><span>Services</span></span></h2>
  <div class="svc-list abs" style="top:197px"><h4>In Town <em>Local Towing</em></h4><p>Most small cars and light trucks in town</p></div>
  <div class="svc-list abs" style="top:268px"><h4>Tire <em>Change</em></h4><p>Change tire on most small cars and light trucks</p></div>
  <div class="svc-list abs" style="top:352px"><h4>Door <em>Unlock</em></h4><p>Unlock most car and light truck doors</p></div>
  <div class="feature-photo abs" role="img" aria-label="Lifted grey off-road vehicle on a service lift in the shop"></div>
  <div class="tab abs" style="left:872px;background:var(--red)"><span>Towing Services</span></div>
  <div class="tab abs" style="left:940px;background:var(--blue)"><span>Routine Service</span></div>
  <div class="tab abs" style="left:1007px;background:var(--blue)"><span>Repairs</span></div>
</section>

<section class="blog">
  <h2 class="sec-title abs">Recent <span class="hl"><span>Blog</span></span></h2>
  <div class="tagline abs">ANYWHERE, ANYTIME TOWING</div>
  <article class="post abs" style="left:130px"><div class="post-photo" role="img" aria-label="Tow truck recovering a vehicle on a snowy road" style="background:linear-gradient(150deg,#e5e8ec,#9aa2ad)"></div><div class="post-rule"></div><h3>Excepteur sint occaecat cupidatat</h3><p>Sed ut perspiciatis unde omnis iste natus error sit voluptatem accusantium doloremque</p><div class="btn">Read More</div></article>
  <article class="post abs" style="left:449px"><div class="post-photo" role="img" aria-label="Truck raised on blue lifts in the repair bay"></div><div class="post-rule"></div><h3>Excepteur sint occaecat cupidatat</h3><p>Sed ut perspiciatis unde omnis iste natus error sit voluptatem accusantium doloremque</p><div class="btn">Read More</div></article>
  <article class="post abs" style="left:769px"><div class="post-photo" role="img" aria-label="Dump truck with raised bed being serviced in the shop"></div><div class="post-rule"></div><h3>Excepteur sint occaecat cupidatat</h3><p>Sed ut perspiciatis unde omnis iste natus error sit voluptatem accusantium doloremque</p><div class="btn">Read More</div></article>
</section>

<section class="split">
  <div class="join abs">
    <h2>JOIN OUR <span class="hl"><span>Team</span></span></h2>
    <div class="sub">Pro inimicus sapientem cibo velit mollis mei</div>
    <p>Doner hamburger elit magna fatback salami. Picanha ad reprehenderit anim pancetta alcatra ham tempor meatloaf shankle do sunt drumstick. Venison bresaola laboris, jowl do labore pastrami magna voluptate fatback sed cow. In beef ribs shankle hamburger beef, ea turkey cupim venison Jowl pig ut biltong sint do capicola ham.</p>
    <div class="btn" style="left:282px;top:308px;width:96px;height:34px">Submit</div>
  </div>
  <div class="quote abs">
    <h2>GET A <span class="hl"><span>Quote</span></span></h2>
    <div class="sub">Pro inimicus sapientem cibo velit mollis mei</div>
    <div class="field" style="left:71px;top:141px;width:194px;height:34px">First Name:</div>
    <div class="field" style="left:275px;top:141px;width:195px;height:34px">Last Name:</div>
    <div class="field" style="left:71px;top:186px;width:194px;height:34px">Email:</div>
    <div class="field" style="left:275px;top:186px;width:195px;height:34px">Phone:</div>
    <div class="field" style="left:71px;top:229px;width:399px;height:66px">Message:</div>
    <div class="btn" style="left:222px;top:308px;width:97px;height:34px">Submit</div>
  </div>
  <div class="hook abs" role="img" aria-label="Yellow tow hook hanging from the top edge"></div>
</section>

<section class="testimonial" role="img" aria-label="Faded portraits of customers in the background">
  <svg class="abs" style="left:48px;top:122px" width="36" height="72" viewBox="0 0 36 72"><path d="M34 2L2 36l32 34" fill="none" stroke="#222" stroke-width="2"/></svg>
  <svg class="abs" style="left:1116px;top:122px" width="36" height="72" viewBox="0 0 36 72"><path d="M2 2l32 34L2 70" fill="none" stroke="#222" stroke-width="2"/></svg>
  <div class="avatar abs" role="img" aria-label="Customer portrait"></div>
  <blockquote>Sed ut perspiciatis unde omnis iste natus error sit voluptatem accusantium doloremque laudantium, totam rem aperiam, eaque ipsa quae ab illo inventore veritatis et quasi architecto beatae vitae dicta sunt explicabo. Nemo enim ipsam voluptatem quia voluptas sit aspernatur aut odit aut fugit, sed quia consequuntur magni dolores eos qui ratione voluptatem sequi nesciunt.</blockquote>
  <h5>DANIEL MARSH</h5>
  <div class="role abs">Director</div>
</section>

<footer class="site-footer">
  <div class="footer-brand abs"><i></i>RIDGELINE REPAIR &amp; TOWING</div>
  <p class="footer-about abs">Repair technicians are on the essential list of the Dept of Public Safety and Ridgeline Repair &amp; Towing is still open during this time.</p>
  <span class="social abs" style="left:130px" aria-label="Social profile"></span>
  <span class="social abs" style="left:172px" aria-label="Social profile"></span>
  <span class="social abs" style="left:212px" aria-label="Social profile"></span>
  <div class="fcol abs" style="left:529px"><h6>Quick <em>Links</em></h6><ul><li>Home</li><li>About Us</li><li>Monthley Coupons</li><li>Services</li><li>More...</li></ul></div>
  <div class="fcol abs" style="left:690px"><h6>Our <em>Services</em></h6><ul><li>Towing Services</li><li>Routine Service</li><li>Repairs</li></ul></div>
  <div class="fcol abs" style="left:850px;width:230px"><h6>Contcat <em>Us</em></h6>
    <div class="citem"><i><svg width="10" height="13" viewBox="0 0 10 13"><path d="M5 12S1 7 1 5a4 4 0 018 0c0 2-4 7-4 7z" fill="#fff"/><circle cx="5" cy="5" r="1.5" fill="#e5173f"/></svg></i>2140 Quarry Lane, Millbrook, Ohio 44000, United States</div>
    <div class="citem"><i><svg width="11" height="11" viewBox="0 0 20 20"><path d="M4 1l4 4-2 3c1 3 3 5 6 6l3-2 4 4-3 3C8 18 2 12 1 4z" fill="#fff"/></svg></i>555-018-2740</div>
  </div>
  <div class="newsletter abs">Enter Your Email:<i><svg width="11" height="11" viewBox="0 0 12 12"><path d="M1 6l10-5-3 10-2-4z" fill="#fff"/></svg></i></div>
  <div class="footer-rule abs"></div>
  <div class="copy abs">COPYRIGHT © 2022 <em>RIDGELINE REPAIR AND TOWING</em>. ALL RIGHTS RESERVED.</div>
</footer>

</body>
</html>
```